Psychology and Counselling Relationship Centre wants a Website

We need a SEO Website that is professional and simple Company Logo and colours is done and supplied

Target Market(s)

People wanting marriage Counselling / Parenting Issues / Relationship issues

Industry/Entity Type

Psychology

Coding

Coded - Design and coding required

Number of Pages Required

5+ page

Font styles to use
Other font styles liked:
• calibri

Colors
32a6d6
33b8a4
0758a5

Requirements
Must have
• Simple easy layout
• Page by page link
• Easy to navigate
• Professional and Welcoming

```html
<!DOCTYPE html>
<html lang="en">
<head>
<meta charset="utf-8">
<title>Relationship Counselling – Whole Heart Living</title>
<link href="https://fonts.googleapis.com/css2?family=Poppins:wght@400;500;600;700&display=swap" rel="stylesheet">
<style>
  :root{
    --blue:#2f74bd;
    --teal:#33b8a4;
    --green:#9cc93a;
    --ink:#111;
    --body:#222;
    --footer:#222222;
    --footer-text:#e6e6e6;
    --muted:#9a9a9a;
    --rule:#3a3a3a;
  }
  *{margin:0;padding:0;box-sizing:border-box}
  html,body{width:980px;height:1200px;overflow:hidden;background:#fff}
  body{position:relative;font-family:"Poppins",sans-serif;color:var(--body)}
  .abs{position:absolute}

  /* header */
  .brand{left:191px;top:52px;display:flex;align-items:center;gap:6px}
  .brand-dot{width:11px;height:11px;border-radius:50%;background:var(--blue)}
  .brand-name{font-weight:700;font-size:10px;color:var(--blue);line-height:1}
  .brand-tag{left:191px;top:65px;font-size:4.6px;color:#777;font-weight:600;letter-spacing:.1px}
  .contact-bar{top:21px;right:191px;display:flex;gap:14px;align-items:center;font-size:8.2px}
  .contact-bar span{display:flex;align-items:center;gap:5px}
  .contact-bar b{font-weight:600}
  .ico{width:14px;height:14px;border-radius:50%;background:var(--blue);display:inline-flex;align-items:center;justify-content:center}
  .nav{top:51px;right:191px;display:flex;align-items:center;font-size:7.6px;font-weight:600;color:var(--ink)}
  .nav a{padding:0 7px;line-height:20px;text-decoration:none;color:inherit}
  .nav a.active{background:var(--blue);color:#fff;border-radius:10px;padding:0 9px}

  /* banner */
  .banner{left:0;top:86px;width:980px;height:70px;background:linear-gradient(90deg,#1a1c22 0%,#2b2e35 45%,#6b7079 75%,#8a9099 100%)}
  .banner-title{left:191px;top:118px;color:#fff;font-weight:600;font-size:10px}
  .crumbs{right:191px;top:118px;font-size:7.5px;color:#fff}
  .crumbs em{font-style:normal;color:var(--teal)}
  .crumbs i{font-style:normal;margin:0 10px}

  /* intro */
  .hero-photo{left:191px;top:203px;width:270px;height:228px;border-radius:6px;background:linear-gradient(135deg,#9fb3c6 0%,#c9b9aa 55%,#6b717a 100%)}
  .intro{left:497px;top:196px;width:292px}
  .intro h1{font-size:21px;font-weight:600;color:var(--ink);line-height:26px}
  .intro h1 span{color:var(--blue)}
  .accent{width:36px;height:2px;background:var(--green);margin:9px 0 17px}
  .intro p{font-size:8.7px;line-height:14.3px;margin-bottom:14.3px}
  .intro a{color:var(--blue);text-decoration:underline}

  .benefits-title{left:191px;top:485px;font-size:11px;font-weight:600;color:var(--ink)}
  .benefits{left:191px;top:514px;list-style:none}
  .benefits li{height:18.36px;display:flex;align-items:center;gap:9px;font-size:8.6px;font-weight:600;color:var(--blue)}
  .leaf{width:10px;height:9px;border-radius:50%;background:var(--green)}

  /* footer */
  .footer{left:0;top:886px;width:980px;height:314px;background:var(--footer);color:var(--footer-text)}
  .f-brand{left:191px;top:75px;display:flex;align-items:center;gap:6px}
  .f-brand .brand-name{font-size:9.5px}
  .f-tag{left:191px;top:88px;font-size:4.4px;color:var(--muted);font-weight:600}
  .f-about{left:193px;top:105px;width:150px;font-size:7.4px;line-height:12.3px}
  .socials{left:192px;top:200px;display:flex;gap:5px}
  .socials span{width:20px;height:20px;border-radius:50%;border:1px solid var(--blue)}
  .f-col h4{font-size:9px;font-weight:600;color:#fff;margin-bottom:14px}
  .f-col ul{list-style:none}
  .f-col li{height:18.36px;font-size:7.5px;display:flex;align-items:center}
  .f-col li::before{content:"";width:6px;height:1px;background:var(--blue);margin-right:9px}
  .f-contact{left:649px;top:38px}
  .f-contact h4{font-size:9px;font-weight:600;color:#fff}
  .ci{position:absolute;left:0;display:flex;gap:8px;font-size:7.5px;line-height:14.3px;white-space:nowrap}
  .f-rule{left:192px;top:246px;width:597px;height:1px;background:var(--rule)}
  .copy{left:194px;top:270px;font-size:7.4px}
  .copy span{color:var(--blue)}
  .legal{right:191px;top:270px;font-size:7.4px}
  .legal i{font-style:normal;margin:0 8px;color:var(--muted)}
</style>
</head>
<body>

<header>
  <div class="abs brand"><div class="brand-dot"></div><div class="brand-name">WHOLE HEART LIVING</div></div>
  <div class="abs brand-tag">PSYCHOLOGY &amp; COUNSELLING RELATIONSHIP CENTRE</div>

  <div class="abs contact-bar">
    <span><i class="ico"><svg width="8" height="6" viewBox="0 0 8 6"><rect x=".5" y=".5" width="7" height="5" fill="none" stroke="#fff"/><path d="M.5 .5 4 3.3 7.5 .5" fill="none" stroke="#fff"/></svg></i>info@wholeheartliving.com.au</span>
    <span><i class="ico"><svg width="8" height="8" viewBox="0 0 8 8"><path d="M1.5 .8 3 2.6 2.2 3.6Q3.4 5 4.6 5.8L5.5 5 7.2 6.5 6.4 7.4Q3.4 7 .6 1.8Z" fill="#fff"/></svg></i><b>(02) 5550 0142</b></span>
    <span><i class="ico"><svg width="6" height="9" viewBox="0 0 6 9"><rect x=".6" y=".6" width="4.8" height="7.8" rx="1" fill="none" stroke="#fff"/><circle cx="3" cy="7" r=".6" fill="#fff"/></svg></i><b>0400 555 000, 0400 555 012</b></span>
  </div>

  <nav class="abs nav">
    <a>HOW WE CAN HELP</a>
    <a class="active">RELATIONSHIP COUNSELLING</a>
    <a>PARENTING</a>
    <a>COURSES</a>
    <a>OUR TEAM</a>
    <a style="padding-right:0">CONTACT</a>
  </nav>
</header>

<div class="abs banner" role="img" aria-label="Background photo of a counsellor writing notes on a clipboard"></div>
<div class="abs banner-title">RELATIONSHIP COUNSELLING</div>
<div class="abs crumbs">Home<i>›</i><em>Relationship Counselling</em></div>

<main>
  <div class="abs hero-photo" role="img" aria-label="Photo of a couple talking with a counsellor"></div>

  <section class="abs intro">
    <h1>Relationship <span>Counselling</span></h1>
    <div class="accent"></div>
    <p>Whole Heart Living Psychology and Counselling Relationship Centre offers experienced Relationship Experts to help you with any relationship issues you are facing.</p>
    <p>Below is a list of issues we can assist you with. Please <a>contact us</a> if you have any questions.</p>
    <p>Relationships can be one of the most enriching, joyful and rewarding experiences in life.</p>
    <p>They can also be quite challenging. Whether you have particular challenges you are facing, or you want to double check your relationship has the key ingredients to living a full and happy life together, coming to therapy can be a positive step towards looking after your relationship.</p>
  </section>

  <h2 class="abs benefits-title">Here are just some of the ways you and your partner can benefit from working with a therapist:</h2>
  <ul class="abs benefits">
    <li><i class="leaf"></i>General relationship or couples counselling</li>
    <li><i class="leaf"></i>Marriage counselling</li>
    <li><i class="leaf"></i>Pre-marriage counselling</li>
    <li><i class="leaf"></i>Parenting issues</li>
    <li><i class="leaf"></i>Dealing with affairs</li>
    <li><i class="leaf"></i>Abusive relationships</li>
    <li><i class="leaf"></i>Feeling Controlled</li>
    <li><i class="leaf"></i>Improve communication</li>
    <li><i class="leaf"></i>Manage arguments or conflict</li>
    <li><i class="leaf"></i>Separation counselling</li>
    <li><i class="leaf"></i>Resolving past issues</li>
    <li><i class="leaf"></i>Gaining a better understanding of each other</li>
    <li><i class="leaf"></i>Discuss future goals</li>
    <li><i class="leaf"></i>Renew common interests</li>
    <li><i class="leaf"></i>Spend more time together</li>
    <li><i class="leaf"></i>Balance self-care with the demands of family life and relationship time</li>
    <li><i class="leaf"></i>Increase intimacy and joy</li>
    <li><i class="leaf"></i>Have more fun together</li>
  </ul>
</main>

<footer class="abs footer">
  <div class="abs f-brand"><div class="brand-dot"></div><div class="brand-name">WHOLE HEART LIVING</div></div>
  <div class="abs f-tag">PSYCHOLOGY &amp; COUNSELLING RELATIONSHIP CENTRE</div>
  <p class="abs f-about">Whole Heart Living Psychology and Counselling Relationship Centre is a team of highly trained professionals providing the ultimate in wellbeing treatment for Relationships: couple, parent and baby, child and parent, men isolated from feelings.</p>
  <div class="abs socials"><span></span><span></span><span></span><span></span></div>

  <div class="abs f-col" style="left:378px;top:38px">
    <h4>QUICK LINKS</h4>
    <ul><li>Home</li><li>How We Can Help</li><li>Relationship Counselling</li><li>Parenting</li><li>Courses</li><li>Our Team</li><li>Contact</li></ul>
  </div>
  <div class="abs f-col" style="left:515px;top:38px">
    <h4>SERVICES</h4>
    <ul><li>Couples</li><li>Parenting</li><li>Adults</li><li>Children &amp; Teenagers</li></ul>
  </div>
  <div class="abs f-contact">
    <h4>CONTACT INFO</h4>
    <div class="ci" style="top:28px"><svg width="12" height="17" viewBox="0 0 12 17"><path d="M6 16C2 10 1 8 1 6a5 5 0 0 1 10 0c0 2-1 4-5 10Z" fill="none" stroke="#2f74bd"/><circle cx="6" cy="6" r="2" fill="none" stroke="#2f74bd"/></svg><span>123, Street Address<br>City</span></div>
    <div class="ci" style="top:69px"><svg width="12" height="17" viewBox="0 0 12 17"><rect x="1" y=".5" width="10" height="16" rx="1.5" fill="none" stroke="#2f74bd"/><rect x="3" y="3" width="6" height="9" fill="none" stroke="#2f74bd"/></svg><span>(02) 5550 0142<br>0400 555 000<br>0400 555 012</span></div>
    <div class="ci" style="top:124px;left:-2px"><svg width="16" height="16" viewBox="0 0 16 16"><rect x="1" y="5" width="14" height="10" fill="none" stroke="#2f74bd"/><path d="M1 5 8 11 15 5M4 5V2h8v3" fill="none" stroke="#2f74bd"/></svg><span>info@wholeheartliving.com.au</span></div>
  </div>

  <div class="abs f-rule"></div>
  <p class="abs copy">Copyright © 2019 <span>Whole Heart Living</span>. All Right Reserved.</p>
  <p class="abs legal">Terms &amp; Condition<i>|</i>Privacy Policy</p>
</footer>

</body>
</html>
```